Edit of flyers - text to be eddited

I currently have three flyers already designed, but want to edit the text on them. On the front of each flyer I want to delete the text which states: "50% off lawn mowing applies to first lawn mowed on any regular service and applies to first 100 callers so call now" and replace it with "Professional Lawn and Garden Maintenance".

Also on the front and rear of each flyer I want to replace the text which states "Tom and Marcus" with "Marcus Fellowes."

All other details can stay the same thanks. I need each of the files saved as a pdf according to the instructions attached with the bleed area set as specified for printing.

Font styles to use
Serif

Colors
acd036
fbed22

Requirements
Must have
• On the front of each flyer I want to delete the text which states: "50% off lawn mowing applies to first lawn mowed on any regular service and applies to first 100 callers so call now" and replace it with "Professional Lawn and Garden Maintenance".
• Also on the front and rear of each flyer I want to replace the text which states "Tom and Marcus" with "Marcus Fellowes."
• All other details can stay the same thanks. I need each of the files saved as a pdf according to the instructions attached with the bleed area set as specified for printing.

```html
<!DOCTYPE html>
<html lang="en">
<head>
<meta charset="utf-8">
<title>Meadowline Lawns – Flyer Front and Back</title>
<link rel="stylesheet" href="https://fonts.googleapis.com/css2?family=Alfa+Slab+One&family=Roboto+Condensed:ital,wght@0,400;0,700;1,400;1,700&display=swap">
<style>
  :root {
    --green-dark: #1d6a18;
    --green-mid: #3f9a25;
    --green-light: #acd036;
    --yellow: #fbed22;
    --sky-top: #8fc3ee;
    --sky-bottom: #e9f4fb;
    --text-dark: #1b1b1b;
    --white: #ffffff;
    --page: #ffffff;
  }
  * { box-sizing: border-box; margin: 0; padding: 0; }
  html, body { width: 1200px; height: 1184px; overflow: hidden; background: var(--page); }
  body { position: relative; font-family: "Roboto Condensed", "Arial Narrow", sans-serif; color: var(--text-dark); }

  .flyer { position: absolute; left: 42px; width: 1116px; height: 522px; overflow: hidden; background: var(--white); }
  .flyer--front { top: 33px; }
  .flyer--back { top: 589px; }

  /* front scene */
  .landscape {
    position: absolute; left: 0; top: 0; width: 100%; height: 405px;
    background: linear-gradient(180deg, #5fa8e6 0%, #bfe0f6 38%, #e4f1e0 52%, #8fcf3a 62%, #5fae22 100%);
  }
  .blossom {
    position: absolute; right: 0; top: 0; width: 280px; height: 410px;
    background: radial-gradient(ellipse at 70% 35%, rgba(255,240,245,0.95) 0%, rgba(250,225,232,0.7) 45%, rgba(255,255,255,0) 75%);
  }
  .front-title {
    position: absolute; left: 0; width: 100%; top: 36px; text-align: center;
    font-family: "Alfa Slab One", Georgia, serif; font-size: 54px; line-height: 70px;
    color: var(--green-dark);
    text-shadow: 0 0 4px var(--white), 0 0 4px var(--white), 0 0 6px var(--white), 0 0 10px #e8ffd0;
  }

  /* back sky */
  .sky {
    position: absolute; left: 0; top: 0; width: 100%; height: 405px;
    background: linear-gradient(180deg, var(--sky-top) 0%, #cfe5f5 35%, var(--sky-bottom) 65%, #ffffff 100%);
  }
  .grass-edge {
    position: absolute; left: 0; top: 368px; width: 100%; height: 34px;
    background: linear-gradient(180deg, rgba(120,190,50,0) 0%, #7cc23a 60%, #4f9e22 100%);
  }
  .flower-art {
    position: absolute; left: 825px; top: 173px; width: 243px; height: 210px;
    background: radial-gradient(circle at 72% 38%, #f6c81e 0%, #f2b820 18%, rgba(255,214,60,0.35) 34%, rgba(255,255,255,0) 58%),
                radial-gradient(circle at 12% 12%, rgba(226,110,40,0.6) 0%, rgba(255,255,255,0) 18%);
  }

  .services-intro { position: absolute; left: 57px; top: 52px; font-size: 19px; }
  .services { position: absolute; top: 83px; list-style: none; }
  .services--one { left: 57px; }
  .services--two { left: 345px; }
  .services li { height: 28px; line-height: 28px; font-size: 19px; font-weight: 700; padding-left: 22px; position: relative; }
  .services li::before {
    content: ""; position: absolute; left: 2px; top: 9px; width: 10px; height: 10px;
    background: var(--green-mid); transform: rotate(45deg);
  }
  .services-close { position: absolute; left: 57px; top: 303px; font-size: 16px; line-height: 24px; }

  .back-title {
    position: absolute; left: 570px; width: 546px; top: 42px; text-align: center;
    font-weight: 700; font-size: 62px; line-height: 76px; color: var(--green-mid);
  }
  .back-tagline {
    position: absolute; left: 570px; width: 546px; top: 134px; text-align: center;
    font-style: italic; font-size: 19px;
  }

  /* shared band */
  .stripe { position: absolute; left: 0; top: 401px; width: 100%; height: 6px; background: var(--yellow); }
  .band {
    position: absolute; left: 0; top: 407px; width: 100%; height: 115px;
    background: linear-gradient(180deg, var(--green-light) 0%, #6fb52e 35%, var(--green-mid) 100%);
  }
  .brand {
    position: absolute; left: 0; width: 100%; top: 375px; text-align: center;
    font-weight: 700; font-size: 22px; color: var(--green-dark);
    display: flex; justify-content: center; align-items: center; gap: 10px;
  }
  .brand-box {
    display: inline-flex; align-items: center; gap: 10px;
    background: var(--white); padding: 6px 18px;
  }
  .brand-mark { width: 16px; height: 16px; background: var(--yellow); }

  .contact { position: absolute; left: 40px; width: 262px; top: 436px; text-align: center; }
  .contact-name { font-size: 13px; line-height: 16px; }
  .contact-phone { font-size: 22px; font-weight: 700; line-height: 26px; }
  .contact-email { font-size: 12px; line-height: 16px; }
  .divider { position: absolute; top: 452px; width: 2px; height: 50px; background: var(--text-dark); }
  .divider--left { left: 340px; }
  .divider--right { left: 775px; }
  .band-service {
    position: absolute; left: 342px; width: 433px; top: 462px; text-align: center;
    font-size: 28px; font-weight: 700;
  }
  .band-web {
    position: absolute; left: 777px; width: 339px; top: 460px; text-align: center;
    font-size: 23px; font-weight: 700;
  }
</style>
</head>
<body>

<section class="flyer flyer--front">
  <div class="landscape" role="img" aria-label="Photo of rolling green lawns with houses under a blue sky"></div>
  <div class="blossom" role="img" aria-label="Photo of white blossom branches"></div>
  <h1 class="front-title">Professional Lawn<br>and Garden Maintenance</h1>

  <div class="stripe"></div>
  <div class="band"></div>
  <div class="brand"><span class="brand-box"><span class="brand-mark"></span>Meadowline Lawns</span></div>

  <div class="contact">
    <p class="contact-name">Marcus Fellowes</p>
    <p class="contact-phone">Ph: 0400555217</p>
    <p class="contact-email">Email: meadowlinelawns@mailbox.com</p>
  </div>
  <span class="divider divider--left"></span>
  <p class="band-service">Lawn &amp; Garden Maintenance</p>
  <span class="divider divider--right"></span>
  <p class="band-web">www.meadowlinelawns.com.au</p>
</section>

<section class="flyer flyer--back">
  <div class="sky"></div>
  <div class="flower-art" role="img" aria-label="Illustration of a butterfly and a yellow daisy"></div>
  <div class="grass-edge" role="img" aria-label="Illustration of a grass edge"></div>

  <p class="services-intro">At Meadowline Lawns we specialise in the following services;</p>
  <ul class="services services--one">
    <li>Lawn mowing</li>
    <li>Blowing</li>
    <li>Pruning</li>
    <li>Weeding</li>
    <li>Mulching</li>
    <li>Rubbish removal</li>
    <li>Lawn care and advice</li>
  </ul>
  <ul class="services services--two">
    <li>Edging</li>
    <li>Hedging</li>
    <li>Tree Loping</li>
    <li>Poisoning</li>
    <li>Fertilising</li>
    <li>Planting</li>
    <li>Turf</li>
  </ul>
  <p class="services-close">And any other garden maintenance job,<br>No job too big or too small.</p>

  <h2 class="back-title">Meadowline Lawns</h2>
  <p class="back-tagline">Professional lawn mowing at an affordable price</p>

  <div class="stripe"></div>
  <div class="band"></div>
  <div class="brand"><span class="brand-box"><span class="brand-mark"></span>Meadowline Lawns</span></div>

  <div class="contact">
    <p class="contact-name">Marcus Fellowes</p>
    <p class="contact-phone">Ph: 0400555217</p>
    <p class="contact-email">Email: meadowlinelawns@mailbox.com</p>
  </div>
  <span class="divider divider--left"></span>
  <p class="band-service">Lawn &amp; Garden Maintenance</p>
  <span class="divider divider--right"></span>
  <p class="band-web">www.meadowlinelawns.com.au</p>
</section>

</body>
</html>
```